Course Graduation Certificate

This project is not for a flyer but instead for the creation of a course graduation certificate. The final certificate needs to include the Marlowe Summit Aviation Academy logo and the text stating as follows:
Certifies that ___________________________ has satisfactorily completed the course of _______________________________ on ________________________________
I would also like to include some type of gold seal of completion as well as a place to sign my name and credentials at the bottom of the certificate
I have included the Marlowe Summit Aviation Academy logo as well as three other certificate examples for you to work from.
Target Market(s)
Students completing a certification course and receiving a certificate
Look and feel

```html
<!DOCTYPE html>
<html lang="en">
<head>
<meta charset="utf-8">
<title>Marlowe Summit Aviation Academy – Course Graduation Certificate</title>
<link rel="stylesheet" href="https://fonts.googleapis.com/css2?family=Gabriela&family=Barlow:wght@600&display=swap">
<style>
  :root {
    --backdrop: #b0b0b0;
    --mount: #333333;
    --gold: #a8844f;
    --paper: #ffffff;
    --ink: #111111;
    --ink-soft: #444444;
    --ornament: #d6d6d6;
    --mark: #eef3f8;
  }
  * { margin: 0; padding: 0; box-sizing: border-box; }
  html, body { width: 1200px; height: 1200px; overflow: hidden; background: var(--backdrop); }
  .canvas { position: relative; width: 1200px; height: 1200px; }
  .mount { position: absolute; left: 58px; top: 217px; width: 1083px; height: 765px; background: var(--mount); }
  .frame { position: absolute; left: 0; top: 0; }
  .ornament { position: absolute; width: 190px; height: 185px; }
  .ornament--tl { left: 108px; top: 264px; background: radial-gradient(circle at 20% 20%, var(--ornament), rgba(214,214,214,0) 70%); }
  .ornament--tr { right: 108px; top: 264px; background: radial-gradient(circle at 80% 20%, var(--ornament), rgba(214,214,214,0) 70%); }
  .ornament--bl { left: 108px; top: 754px; background: radial-gradient(circle at 20% 80%, var(--ornament), rgba(214,214,214,0) 70%); }
  .ornament--br { right: 108px; top: 754px; background: radial-gradient(circle at 80% 80%, var(--ornament), rgba(214,214,214,0) 70%); }
  .brand-mark { position: absolute; left: 0; width: 1200px; top: 548px; text-align: center;
    font-family: 'Gabriela', serif; font-size: 92px; color: var(--mark); letter-spacing: 6px; white-space: nowrap; }
  .title { position: absolute; left: 0; width: 1200px; text-align: center; font-family: 'Gabriela', serif;
    color: var(--ink-soft); font-size: 46px; line-height: 1; white-space: nowrap; letter-spacing: -1px; }
  .title--academy { top: 330px; font-size: 40px; }
  .title--certificate { top: 398px; font-size: 50px; }
  .subtitle { position: absolute; left: 0; width: 1200px; top: 464px; text-align: center;
    font-family: 'Barlow', sans-serif; font-weight: 600; font-size: 23px; letter-spacing: 4px; color: var(--gold); }
  .rule { position: absolute; top: 476px; width: 78px; height: 3px; border-radius: 50%; background: var(--gold); }
  .rule--left { left: 335px; }
  .rule--right { left: 786px; }
  .statement { position: absolute; left: 259px; top: 540px; width: 720px; font-family: 'Gabriela', serif;
    font-size: 42px; line-height: 74px; color: var(--ink); white-space: nowrap; }
  .blank { display: inline-block; border-bottom: 2px solid var(--ink); vertical-align: baseline; height: 1px; }
  .blank--name { width: 170px; margin: 0 0 0 8px; }
  .blank--course { width: 92px; }
  .blank--day { width: 108px; }
  .sign-line { position: absolute; top: 841px; height: 2px; background: var(--ink); }
  .sign-line--date { left: 361px; width: 171px; }
  .sign-line--signature { left: 653px; width: 259px; }
  .sign-label { position: absolute; top: 860px; font-family: 'Gabriela', serif; font-size: 22px;
    letter-spacing: 2px; color: var(--ink-soft); text-align: center; }
  .sign-label--date { left: 361px; width: 171px; }
  .sign-label--signature { left: 653px; width: 295px; }
</style>
</head>
<body>
<main class="canvas">
  <div class="mount"></div>
  <svg class="frame" width="1200" height="1200" viewBox="0 0 1200 1200" aria-hidden="true">
    <path fill="var(--gold)" d="M110 235 L1090 235 A34 34 0 0 0 1124 269 L1124 931 A34 34 0 0 0 1090 965 L110 965 A34 34 0 0 0 76 931 L76 269 A34 34 0 0 0 110 235 Z"/>
    <path fill="var(--paper)" d="M115 241 L1085 241 A34 34 0 0 0 1119 275 L1119 925 A34 34 0 0 0 1085 959 L115 959 A34 34 0 0 0 81 925 L81 275 A34 34 0 0 0 115 241 Z"/>
    <path fill="none" stroke="var(--gold)" stroke-width="2.5" d="M124 252 L1076 252 A31 31 0 0 0 1107 283 L1107 917 A31 31 0 0 0 1076 948 L124 948 A31 31 0 0 0 93 917 L93 283 A31 31 0 0 0 124 252 Z"/>
  </svg>

  <div class="ornament ornament--tl" role="img" aria-label="Silver filigree scroll ornament, top left corner"></div>
  <div class="ornament ornament--tr" role="img" aria-label="Silver filigree scroll ornament, top right corner"></div>
  <div class="ornament ornament--bl" role="img" aria-label="Silver filigree scroll ornament, bottom left corner"></div>
  <div class="ornament ornament--br" role="img" aria-label="Silver filigree scroll ornament, bottom right corner"></div>

  <div class="brand-mark" aria-hidden="true">MARLOWE SUMMIT</div>

  <h1 class="title title--academy">MARLOWE SUMMIT AVIATION ACADEMY</h1>
  <div class="title title--certificate">CERTIFICATE</div>
  <span class="rule rule--left"></span>
  <p class="subtitle">OF COURSE GRADUATION</p>
  <span class="rule rule--right"></span>

  <p class="statement">
    Certifies that<span class="blank blank--name"></span>has satisfactorily<br>
    completed the course of<span class="blank blank--course"></span>on<span class="blank blank--day"></span>
  </p>

  <span class="sign-line sign-line--date"></span>
  <span class="sign-line sign-line--signature"></span>
  <p class="sign-label sign-label--date">DATE</p>
  <p class="sign-label sign-label--signature">SIGNATURE</p>
</main>
</body>
</html>
```